Pain Management, Personal Injury & Motor Vehicle Accident

I need t rack card to use as marketing collateral while talking to urgent cares, wreckers services, primary care, and emergency room staff
If you have been involved in a motor vehicle accident or personal injury accident, Prairie Ridge Pain Specialist is your Solution to complete pain relief. We understand your pain and are here to assist you along the journey to becoming pain free. It is crucial that you choose a physician who is experienced in treating your unique injury.
At Prairie Ridge Pain Specialist, Dr Calvin Hardesty and his team of experts will provide you with a specialized approach to reducing and managing your pain with a comprehensive and effective treatment plan based on a proper diagnosis. You can expect an exceptional treatment program for your injuries to help you to begin improving your quality of life immediately.
We treat:
Car Accident Injuries
Semi Truck Injuries
Most Personal Injuries
Slip and Falls
Motorcycle Accident Injuries
Whiplash
Back Injuries
Neck Injuries
Shoulder Injuries
Headaches
Locations: Cedar Bluff, Millbrook, Haskett
Phone: (580) 472-6193
Fax: (833) 748-2954
www.prairieridgepainclinic.com
Target Market(s)
Urgent Cares, Emergency Rooms, Primary Care, Wrecker Services, anyone involved in a Personal Injury or Motor Vehicle Accident
Industry/Entity Type
Healthcare, Motor Vehicle Accident Injury, Personal Injury, Pain Management, Pain Relief

```html
<!DOCTYPE html>
<html lang="en">
<head>
<meta charset="utf-8">
<title>Prairie Ridge Pain Specialist – Rack Card</title>
<link rel="stylesheet" href="https://fonts.googleapis.com/css2?family=Open+Sans:wght@400;600;700&display=swap">
<style>
  :root {
    --stage: #2b2b2b;
    --card-light: #f4f4f5;
    --card-mid: #c4c5c8;
    --ink: #1c1c1c;
    --red: #d8262e;
    --photo-light: #d9d6d4;
    --photo-dark: #6d6866;
    --photo-warm: #e8603a;
  }
  * { box-sizing: border-box; margin: 0; padding: 0; }
  html, body { width: 1111px; height: 1200px; overflow: hidden; }
  body {
    background: var(--stage);
    font-family: "Open Sans", Arial, sans-serif;
    color: var(--ink);
    position: relative;
  }
  .rack-card {
    position: absolute;
    top: 160px;
    width: 391px;
    height: 880px;
    overflow: hidden;
    background: radial-gradient(ellipse at 50% 48%, var(--card-light) 0%, #dcdcde 40%, var(--card-mid) 100%);
  }
  .rack-card--front { left: 122px; }
  .rack-card--back { left: 597px; }

  .brand {
    position: absolute;
    left: 36px;
    top: 78px;
    display: flex;
    align-items: center;
    gap: 10px;
  }
  .brand__dot {
    width: 14px; height: 14px; border-radius: 50%;
    background: var(--red);
    flex: none;
  }
  .brand__name {
    font-size: 13px;
    font-weight: 600;
    line-height: 17px;
    color: var(--ink);
  }

  .intro {
    position: absolute;
    left: 36px;
    top: 200px;
    width: 312px;
    font-size: 10.3px;
    line-height: 15.2px;
  }
  .intro p + p { margin-top: 15px; }

  .art { position: absolute; left: 0; top: 0; width: 391px; height: 880px; }

  .treat-title {
    position: absolute;
    left: 38px;
    top: 80px;
    width: 330px;
    font-size: 17px;
    font-weight: 700;
    padding-bottom: 3px;
    border-bottom: 1.5px solid var(--red);
  }
  .treat-list {
    position: absolute;
    list-style: none;
    font-size: 11.4px;
  }
  .treat-list li {
    height: 38.3px;
    position: relative;
    padding-left: 17px;
  }
  .treat-list li::before {
    content: "";
    position: absolute;
    left: 0; top: 6px;
    width: 3.5px; height: 3.5px; border-radius: 50%;
    background: var(--ink);
  }
  .treat-list--left { left: 38px; top: 114px; }
  .treat-list--right { left: 260px; top: 114px; }

  .contact {
    position: absolute;
    left: 38px;
    top: 360px;
    border-left: 1.5px solid var(--red);
    padding-left: 7px;
    list-style: none;
    font-size: 13px;
  }
  .contact li {
    display: flex;
    align-items: center;
    gap: 6px;
    height: 23px;
  }
  .contact svg { width: 12px; height: 12px; flex: none; }
</style>
</head>
<body>

<section class="rack-card rack-card--front">
  <div class="brand">
    <span class="brand__dot"></span>
    <div class="brand__name">
      Hardesty Medical, LLC dba<br>
      Prairie Ridge Pain Specialists<br>
      Dr. Calvin R. Hardesty, MD
    </div>
  </div>

  <div class="intro">
    <p>If you have been involved in a motor vehicle accident or personal injury accident, Prairie Ridge Pain Specialist is your Solution to complete pain relief. We understand your pain and are here to assist you along the journey to becoming pain free. It is crucial that you choose a physician who is experienced in treating your unique injury.</p>
    <p>At Prairie Ridge Pain Specialist, Dr Calvin Hardesty and his team of experts will provide you with a specialized approach to reducing and managing your pain with a comprehensive and effective treatment plan based on a proper diagnosis. You can expect an exceptional treatment program for your injuries to help you to begin improving your quality of life immediately.</p>
  </div>

  <svg class="art" viewBox="0 0 391 880">
    <defs>
      <radialGradient id="backGlow" cx="0.5" cy="0.75" r="0.6">
        <stop offset="0" stop-color="var(--photo-warm)"/>
        <stop offset="0.35" stop-color="#b98d80"/>
        <stop offset="1" stop-color="var(--photo-dark)"/>
      </radialGradient>
      <radialGradient id="backGlowSmall" cx="0.5" cy="0.7" r="0.5">
        <stop offset="0" stop-color="var(--red)"/>
        <stop offset="1" stop-color="#7a7674"/>
      </radialGradient>
    </defs>
    <path role="img" aria-label="Photo of a man holding his lower back, with the painful area glowing red"
          d="M0,652 C120,656 205,625 255,560 C295,505 330,470 391,440 L391,880 L0,880 Z"
          fill="url(#backGlow)"/>
    <path d="M0,652 C120,656 205,625 255,560 C295,505 330,470 391,440"
          fill="none" stroke="var(--red)" stroke-width="14"/>
    <circle role="img" aria-label="Close photo of a man's bare back with a glowing red spine"
            cx="304" cy="474" r="67" fill="url(#backGlowSmall)"
            stroke="var(--red)" stroke-width="5"/>
  </svg>
</section>

<section class="rack-card rack-card--back">
  <h2 class="treat-title">WE TREAT:</h2>
  <ul class="treat-list treat-list--left">
    <li>Car Accident Injuries</li>
    <li>Semi Truck Injuries</li>
    <li>Most Personal Injuries</li>
    <li>Slip and Falls</li>
    <li>Motorcycle Accident Injuries</li>
  </ul>
  <ul class="treat-list treat-list--right">
    <li>Whiplash</li>
    <li>Back Injuries</li>
    <li>Neck Injuries</li>
    <li>Shoulder Injuries</li>
    <li>Headaches</li>
  </ul>

  <ul class="contact">
    <li>
      <svg viewBox="0 0 12 12"><circle cx="6" cy="6" r="6" fill="var(--red)"/><path d="M6 2.5a2.2 2.2 0 0 0-2.2 2.2C3.8 6.4 6 9.2 6 9.2s2.2-2.8 2.2-4.5A2.2 2.2 0 0 0 6 2.5z" fill="#fff"/><circle cx="6" cy="4.7" r="0.9" fill="var(--red)"/></svg>
      Cedar Bluff, Millbrook, Haskett
    </li>
    <li>
      <svg viewBox="0 0 12 12"><circle cx="6" cy="6" r="6" fill="var(--red)"/><path d="M3.6 3.2l1.2-.3.7 1.5-.8.6c.4.9 1 1.5 1.9 1.9l.6-.8 1.5.7-.3 1.2C6 8.4 3.6 6 3.6 3.2z" fill="#fff"/></svg>
      (580) 472-6193
    </li>
    <li>
      <svg viewBox="0 0 12 12"><circle cx="6" cy="6" r="6" fill="var(--red)"/><rect x="3" y="4" width="6" height="4.5" rx="0.5" fill="#fff"/><rect x="4.2" y="2.8" width="3.6" height="1.6" fill="#fff"/></svg>
      (833) 748-2954
    </li>
    <li>
      <svg viewBox="0 0 12 12"><circle cx="6" cy="6" r="6" fill="var(--red)"/><circle cx="6" cy="6" r="3.3" fill="none" stroke="#fff" stroke-width="0.8"/><path d="M2.7 6h6.6M6 2.7c-1.6 2-1.6 4.6 0 6.6M6 2.7c1.6 2 1.6 4.6 0 6.6" fill="none" stroke="#fff" stroke-width="0.7"/></svg>
      www.prairieridgepainclinic.com
    </li>
  </ul>

  <svg class="art" viewBox="0 0 391 880">
    <defs>
      <radialGradient id="neckGlow" cx="0.35" cy="0.55" r="0.7">
        <stop offset="0" stop-color="#e86a6a"/>
        <stop offset="0.4" stop-color="#e9c2c0"/>
        <stop offset="1" stop-color="var(--photo-light)"/>
      </radialGradient>
      <radialGradient id="neckGlowSmall" cx="0.4" cy="0.6" r="0.6">
        <stop offset="0" stop-color="#e35757"/>
        <stop offset="1" stop-color="#d4d0ce"/>
      </radialGradient>
    </defs>
    <path role="img" aria-label="Photo of a therapist treating a woman's sore neck and shoulder, highlighted in red"
          d="M0,440 C30,485 70,502 115,496 C170,488 205,490 230,515 C260,545 280,600 310,640 C340,660 370,652 391,650 L391,880 L0,880 Z"
          fill="url(#neckGlow)"/>
    <path d="M0,440 C30,485 70,502 115,496 C170,488 205,490 230,515 C260,545 280,600 310,640 C340,660 370,652 391,650"
          fill="none" stroke="var(--red)" stroke-width="6"/>
    <rect x="330" y="642" width="61" height="14" fill="var(--red)"/>
    <circle role="img" aria-label="Close photo of a hand pressing on a painful neck"
            cx="294" cy="590" r="77" fill="url(#neckGlowSmall)"
            stroke="var(--red)" stroke-width="5"/>
  </svg>
</section>

</body>
</html>
```